Varnel Flyer

We need a flyer designed for a Security Company. Our main focus is security consulting and risk management. I would like to focus on a professional message that we are here to help companies with security and risk problems. We are independent and do not affiliate with any other companies.

Who we are:
Over 25+ years of experience in Security and Law Enforcement
Specialize in Security Management
Board Certified in Security management
Accredited defense Specialist (ADS)
We are not affiliated with any security provider or guard company we provide independent advise

Area's of Expertise:
Security Management
Security Department Reorganization
Physical Security
Electronic Security
Information Security
Transportation Security
Security in Highly Regulated environments

Services Offered:

Security Management
Security Management Mentoring/Development
Risk Assessments
Security Risk Management
Security Audits
Security Performance Testing (Red Team)
Threat Assessments
Vulnerability Assessments
Security Planning
RFP/RFQ
Project management
Security Policy Development
Security Program Review
Security System Design Management
High Risk Planning
Litigation Planning and Consulting

What to look for in a Security Consultant:

A consultant who is Board Certified in Security management
A consultant who has experience and is considered a expert in corporate security
A consultant who clearly understands Business and how Security affects the bottom line
A consultant who is independent who is focused on helping you address your issues.
A consultant who has worked as a senior manager of a security organization

Industries:

Energy
Healthcare
Real Estate
Nuclear
Highly secure facilities

Accredited Defense Specialist (ADS)

The Accredited Defense Specialist (ADSⓇ) is considered the “gold standard” certification for security management professionals and demonstrates knowledge and competency in seven key domains of security. Globally recognized as the standard of excellence for security management professionals. The ADS is administered by OPRA Worldwide, which is the predominant international organization for security Internationally.

Contact us:

Phone: 555-271-6043
info@varnelguard.example
www.varnelguard.example

```html
<!DOCTYPE html>
<html lang="en">
<head>
<meta charset="utf-8">
<title>Varnel Flyer</title>
<link href="https://fonts.googleapis.com/css2?family=Montserrat:wght@700;800&family=Lato:ital,wght@0,400;0,700;0,900;1,900&display=swap" rel="stylesheet">
<style>
:root{
  --backdrop:#7a7a7a;
  --paper:#ffffff;
  --blue:#0e5ca3;
  --blue-deep:#0a4a87;
  --ink:#2e2e2e;
  --text:#222;
  --footer:#2a2a2a;
  --grey-panel:#e4e4e4;
}
*{margin:0;padding:0;box-sizing:border-box}
html,body{width:1200px;height:1200px;overflow:hidden;background:var(--backdrop)}
body{font-family:"Lato",sans-serif;color:var(--text)}
.flyer{position:absolute;left:221px;top:68px;width:758px;height:1064px;background:var(--paper);overflow:hidden}
.brand-panel{position:absolute;right:0;top:0;width:390px;height:136px;background:linear-gradient(90deg,#f4f4f4,var(--grey-panel));clip-path:polygon(0 0,100% 0,100% 100%,76px 100%)}
.brand{position:absolute;left:466px;top:40px;display:flex;align-items:center;gap:12px}
.brand-mark{width:40px;height:40px;background:var(--blue)}
.brand-name{font-family:"Montserrat",sans-serif;font-weight:800;font-size:38px;letter-spacing:4px;color:var(--blue-deep)}
.photo{position:absolute;left:0;top:134px;width:758px;height:330px;background:linear-gradient(100deg,#d9dde2 0%,#c2c8d0 35%,#1d3344 55%,#0f2a3a 68%,#e6ecef 80%,#d4d8dc 100%)}
.headline{position:absolute;left:30px;top:24px;font-family:"Montserrat",sans-serif;font-weight:800;line-height:35px}
.headline .lead{color:var(--blue);font-size:27px}
.headline .main{color:var(--ink);font-size:28.5px;display:block}
.photo-rule{position:absolute;left:0;top:464px;width:758px;height:6px;background:var(--blue-deep)}
.pill{position:absolute;display:flex;align-items:center}
.pill-icon{border-radius:50%;background:var(--ink);display:flex;align-items:center;justify-content:center;z-index:1;border:2px solid #fff}
.pill-label{background:var(--blue);color:#fff;font-family:"Montserrat",sans-serif;font-weight:700;text-transform:uppercase;border-radius:0 14px 14px 0;margin-left:-10px;padding-left:18px;letter-spacing:.5px}
.pill-sm .pill-icon{width:34px;height:34px}
.pill-sm .pill-label{font-size:15.5px;height:24px;line-height:24px;padding-right:14px}
.pill-lg .pill-icon{width:56px;height:56px}
.pill-lg .pill-label{font-size:13.5px;line-height:17px;padding:6px 20px 6px 24px;border-radius:0 20px 20px 0;margin-left:-16px}
.list{position:absolute;list-style:none;font-size:13px;line-height:16px}
.list li{position:relative;padding-left:22px}
.list li::before{content:"";position:absolute;left:3px;top:4px;width:8px;height:8px;border-radius:50%;background:var(--blue)}
.who{left:32px;top:526px;width:340px}
.who li{margin-bottom:7px}
.expertise{left:29px;top:711px}
.expertise li{margin-bottom:7.3px}
.lookfor{left:390px;top:545px;width:340px}
.lookfor li{margin-bottom:6px}
.industries{position:absolute;left:34px;top:918px;display:grid;grid-template-columns:164px 160px;row-gap:8px;list-style:none;font-weight:900;font-style:italic;font-size:14px;line-height:16px;color:#111}
.industries li{position:relative;padding-left:22px}
.industries li::before{content:"";position:absolute;left:0;top:4px;width:8px;height:8px;border-radius:50%;background:var(--blue)}
.cert{position:absolute;left:379px;top:751px;width:347px;height:245px}
.cert-title{height:43px;background:linear-gradient(#f2f2f2,#e2e2e2);border-radius:16px 16px 0 0;font-weight:700;font-size:15.5px;line-height:43px;padding-left:24px;color:#111}
.cert-body{background:var(--blue);height:202px;color:#fff;padding:8px 16px 0 16px}
.cert-body p{font-size:12px;line-height:14.8px;text-align:justify}
.cert-badge{display:block;margin:14px auto 0;width:144px;height:44px}
.footer{position:absolute;left:0;top:996px;width:758px;height:68px;background:var(--footer);color:#fff;display:flex;align-items:center}
.contact{position:absolute;display:flex;align-items:center;gap:10px}
.phone{left:30px;font-size:18px}
.email{left:290px;font-size:14.5px}
.web{left:557px;font-size:14.5px}
</style>
</head>
<body>
<div class="flyer">
  <div class="photo" role="img" aria-label="Photo of a consultant on the phone at a desk beside a monitor showing a padlock shield"></div>
  <div class="brand-panel"></div>
  <div class="brand"><span class="brand-mark"></span><span class="brand-name">VARNEL</span></div>
  <h1 class="headline"><span class="lead">Our main focus is</span><span class="main">SECURITY CONSULTING</span><span class="main">&amp; RISK MANAGEMENT</span></h1>
  <div class="photo-rule"></div>

  <div class="pill pill-sm" style="left:26px;top:484px">
    <span class="pill-icon"><svg width="18" height="14" viewBox="0 0 18 14" fill="#fff"><circle cx="9" cy="3.5" r="2.6"/><circle cx="3.5" cy="5" r="2"/><circle cx="14.5" cy="5" r="2"/><path d="M4.5 14v-3.5a4.5 4 0 0 1 9 0V14z"/><path d="M0 14v-2.5a3 3 0 0 1 3.5-3V14zM18 14v-2.5a3 3 0 0 0-3.5-3V14z"/></svg></span>
    <span class="pill-label">Who we are:</span>
  </div>
  <ul class="list who">
    <li>Over 25+ years of experience in Security and Law Enforcement</li>
    <li>Specialize in Security Management</li>
    <li>Board Certified in Security management</li>
    <li>Accredited defense Specialist (ADS)</li>
    <li>We are not affiliated with any security provider or guard company we provide independent advise</li>
  </ul>

  <div class="pill pill-sm" style="left:26px;top:670px">
    <span class="pill-icon"><svg width="16" height="18" viewBox="0 0 16 18" fill="none" stroke="#fff" stroke-width="1.4"><path d="M5 12c0-2-3-3-3-6.5a6 6 0 0 1 12 0C14 9 11 10 11 12z"/><path d="M5.5 14.5h5M6.5 17h3"/></svg></span>
    <span class="pill-label">Area's of expertise:</span>
  </div>
  <ul class="list expertise">
    <li>Security Management</li>
    <li>Security Department Reorganization</li>
    <li>Physical Security</li>
    <li>Electronic Security</li>
    <li>Information Security</li>
    <li>Transportation Security</li>
    <li>Security in Highly Regulated environments</li>
  </ul>

  <div class="pill pill-sm" style="left:26px;top:878px">
    <span class="pill-icon"><svg width="18" height="17" viewBox="0 0 18 17" fill="#fff"><rect x="0" y="7" width="4" height="10" rx="1"/><path d="M5 8l4-7c2 0 2.5 1.5 2 3.5L10.5 7H16a2 2 0 0 1 1.8 2.5l-1.8 6A2 2 0 0 1 14 17H5z"/></svg></span>
    <span class="pill-label">Industries:</span>
  </div>
  <ul class="industries">
    <li>ENERGY</li><li>REAL ESTATE</li>
    <li>HEALTHCARE</li><li>HIGHLY SECURE</li>
    <li>NUCLEAR</li><li>FACILITIES</li>
  </ul>

  <div class="pill pill-lg" style="left:376px;top:479px">
    <span class="pill-icon"><svg width="32" height="32" viewBox="0 0 32 32" fill="none" stroke="#fff" stroke-width="2.6"><circle cx="19" cy="13" r="9"/><path d="M12.5 19.5 3 29" stroke-linecap="round" stroke-width="4"/></svg></span>
    <span class="pill-label">What to look for<br>in a security consultant:</span>
  </div>
  <ul class="list lookfor">
    <li>A consultant who is Board Certified in Security management</li>
    <li>A consultant who has experience and is considered a expert in corporate security</li>
    <li>A consultant who clearly understands Business and how Security affects the bottom line</li>
    <li>A consultant who is independent who is focused on helping you address your issues.</li>
    <li>A consultant who has worked as a senior manager of a security organization</li>
  </ul>

  <section class="cert">
    <h2 class="cert-title">Accredited Defense Specialist (ADS)</h2>
    <div class="cert-body">
      <p>The Accredited Defense Specialist (ADSⓇ) is considered the “gold standard” certification for security management professionals and demonstrates knowledge and competency in seven key domains of security. Globally recognized as the standard of excellence for security management professionals. The ADS is administered by OPRA Worldwide, which is the predominant international organization for security Internationally.</p>
      <svg class="cert-badge" viewBox="0 0 144 44"><rect x="0" y="0" width="144" height="44" rx="6" fill="#fff"/></svg>
    </div>
  </section>

  <footer class="footer">
    <div class="contact phone"><svg width="16" height="16" viewBox="0 0 16 16" fill="#2f7fd0"><path d="M3.5 0.5 6 3.5 4.5 6a9 9 0 0 0 5.5 5.5L12.5 10l3 2.5-1.5 3C7 15.5 0.5 9 0.5 2z"/></svg><span>555-271-6043</span></div>
    <div class="contact email"><svg width="18" height="12" viewBox="0 0 18 12"><rect width="18" height="12" fill="#2f7fd0"/><path d="M0 0l9 7 9-7" fill="none" stroke="#2a2a2a" stroke-width="1.3"/></svg><span>info@varnelguard.example</span></div>
    <div class="contact web"><svg width="14" height="14" viewBox="0 0 14 14" fill="none" stroke="#2f7fd0" stroke-width="1.2"><circle cx="7" cy="7" r="6"/><ellipse cx="7" cy="7" rx="2.6" ry="6"/><path d="M1 7h12"/></svg><span>www.varnelguard.example</span></div>
  </footer>
</div>
</body>
</html>
```